Updated Business Card for Optometry Practice

We're a growing optometry practice that is moving to a beautiful new office and we want to update our business card. We just updated our logo so the new card should reflect the new logo. Our practice continually invests in state of the art instruments to help us provide eye care that is thorough, comfortable, efficient and educational.

I've attached our current card and logo. You can reference this for the information I would like on the card. The tag line on the back is "We're changing the way you see."

Upon completion of this project we will need (amongst other formats) Photoshop files of the card so I can change employee names to print cards for each employee.

```html
<!DOCTYPE html>
<html lang="en">
<head>
<meta charset="UTF-8">
<title>Brightwater Family Eyecare – Business Card</title>
<link rel="stylesheet" href="https://fonts.googleapis.com/css2?family=Montserrat:wght@600&family=Open+Sans:wght@400;600;700&display=swap">
<style>
  :root {
    --navy: #14284d;
    --gold: #d4a82a;
    --grey-text: #6b6f78;
    --card-white: #ffffff;
    --backdrop: #e6e6e8;
  }
  * { margin: 0; padding: 0; box-sizing: border-box; }
  html, body {
    width: 1200px; height: 675px; overflow: hidden;
    background: var(--backdrop);
  }
  .canvas {
    position: relative; width: 1200px; height: 675px;
    display: flex; align-items: center; justify-content: center; gap: 40px;
  }
  .card {
    position: relative; width: 520px; height: 297px;
    box-shadow: 0 6px 18px rgba(0,0,0,0.18);
    overflow: hidden;
  }
  .card--front {
    background: var(--navy);
    display: flex; flex-direction: column; align-items: center; justify-content: center;
  }
  .brand-name {
    font-family: "Montserrat", sans-serif; font-weight: 600;
    letter-spacing: 0.04em; line-height: 1.15; text-align: center;
  }
  .card--front .brand-name { color: #ffffff; font-size: 34px; }
  .brand-lockup { display: flex; align-items: center; gap: 14px; }
  .brand-dot { width: 22px; height: 22px; border-radius: 50%; background: var(--gold); flex: none; }
  .tagline {
    margin-top: 46px;
    font-family: "Open Sans", sans-serif; font-weight: 600;
    font-size: 15px; color: #ffffff; letter-spacing: 0.02em;
  }
  .card--back { background: var(--card-white); }
  .card--back .brand-lockup { position: absolute; left: 34px; top: 34px; }
  .card--back .brand-name { color: var(--navy); font-size: 26px; text-align: left; }
  .person { position: absolute; left: 58px; top: 150px; font-family: "Open Sans", sans-serif; }
  .person__name { font-weight: 700; font-size: 19px; color: var(--navy); }
  .person__title { font-size: 15px; color: var(--gold); margin-top: 2px; }
  .contact-list {
    position: absolute; left: 58px; bottom: 24px; list-style: none;
    font-family: "Open Sans", sans-serif; font-size: 13.5px; color: var(--grey-text);
  }
  .contact-list li { display: flex; align-items: center; gap: 8px; margin-top: 4px; }
  .contact-list svg { width: 16px; height: 16px; flex: none; }
  .practice-address {
    position: absolute; right: 32px; top: 150px; text-align: right;
    font-family: "Open Sans", sans-serif; font-size: 13.5px; color: var(--grey-text); line-height: 1.35;
  }
  .practice-address__name { font-weight: 700; color: var(--navy); }
</style>
</head>
<body>
<main class="canvas">
  <section class="card card--front" aria-label="Card front">
    <div class="brand-lockup">
      <span class="brand-dot"></span>
      <p class="brand-name">Brightwater<br>Family Eyecare</p>
    </div>
    <p class="tagline">We're changing the way you see.</p>
  </section>

  <section class="card card--back" aria-label="Card back">
    <div class="brand-lockup">
      <span class="brand-dot"></span>
      <p class="brand-name">Brightwater<br>Family Eyecare</p>
    </div>

    <div class="person">
      <p class="person__name">Daniel Marsh, OD</p>
      <p class="person__title">Optometrist</p>
    </div>

    <address class="practice-address">
      <span class="practice-address__name">Brightwater Family Eyecare</span><br>
      2750 Linden Park Dr #210<br>
      Brightwater, MO 63000
    </address>

    <ul class="contact-list">
      <li>
        <svg viewBox="0 0 16 16" aria-hidden="true"><circle cx="8" cy="8" r="8" fill="#14284d"/><path d="M5.2 4.2l1.6 0 .6 2-1 .8c.5 1 1.2 1.8 2.2 2.3l.8-1 2 .6v1.6c0 .5-.4.8-.9.8C7.1 11.1 4.9 8.9 4.7 5.1c0-.5.3-.9.5-.9z" fill="#fff"/></svg>
        (555) 014-2290
      </li>
      <li>
        <svg viewBox="0 0 16 16" aria-hidden="true"><circle cx="8" cy="8" r="8" fill="#14284d"/><rect x="4" y="5.2" width="8" height="5.6" fill="none" stroke="#fff" stroke-width="1"/><path d="M4 5.4l4 3 4-3" fill="none" stroke="#fff" stroke-width="1"/></svg>
        dan@brightwatereyecare.com
      </li>
      <li>
        <svg viewBox="0 0 16 16" aria-hidden="true"><circle cx="8" cy="8" r="8" fill="#14284d"/><circle cx="8" cy="8" r="4.6" fill="none" stroke="#fff" stroke-width="0.9"/><ellipse cx="8" cy="8" rx="2" ry="4.6" fill="none" stroke="#fff" stroke-width="0.9"/><path d="M3.4 8h9.2" stroke="#fff" stroke-width="0.9"/></svg>
        www.brightwatereyecare.com
      </li>
    </ul>
  </section>
</main>
</body>
</html>
```